Website for Torvik Capital

We need a new web design for a company based in Chicago called "Torvik Capital". TVK provides portfolio management and financial advice using primarily income oriented strategies, such as, dividend paying stocks and preferred stocks. Our niche is utilizing conservative option strategies to help generate income and minimize risk. We are looking for a clean-cut and streamline professional site that is both appealing and user friendly. We would like the main colors to be the dark blue and bright green of our logo. Depending on cost and ease, we may want a designer to give us the completed website, including the coding, etc.

Target Market(s)

20-80 year old affluent investors seeking portfolio management and investment advice.

Industry/Entity Type

Conservative

Requirements
Must have
• -our logo
-main tabs: home, about us, our philosophy, our services, investment strategy, compliance, contact us
-our phone number visible and conveniently placed on each page
Nice to have
• -conveniently placed login button for current clients
-conveniently placed "quick contact" box on home page with spaces for first name, last name, email, phone number, and a blank box for their question or comment
-check us out on plain square and plain square logos/buttons
-we like the idea of rotating pictures on top of page, but we aren't sure whether or not we definitely want that
Should not have
• -no trees
-no clocks
-no timers
-no crowns
-no plants

```html
<!DOCTYPE html>
<html lang="en">
<head>
<meta charset="utf-8">
<title>Torvik Capital</title>
<link href="https://fonts.googleapis.com/css2?family=Ubuntu:wght@400;500&family=Cinzel:wght@400&family=Arimo:wght@400;700&display=swap" rel="stylesheet">
<style>
:root{
  --navy:#0a1670;
  --blue:#0a52d0;
  --blue-light:#0b6fe6;
  --blue-deep:#0a2c96;
  --green:#8fd61c;
  --green-dark:#6bb212;
  --ink:#0e1a2a;
  --panel:#101b2b;
  --red:#e8000b;
  --white:#ffffff;
  --line:#c9c9c9;
  --muted:#5c6673;
}
*{box-sizing:border-box;margin:0;padding:0}
html,body{width:1074px;height:1200px;overflow:hidden}
body{position:relative;background:var(--white);font-family:"Ubuntu",sans-serif;color:var(--ink)}
.stage-band{position:absolute;left:0;top:164px;width:1074px;height:922px;background:linear-gradient(180deg,var(--blue-light) 0%,var(--blue) 45%,var(--blue-deep) 100%)}
.header{position:absolute;left:0;top:0;width:1074px;height:124px;background:var(--white)}
.brand{position:absolute;left:80px;top:50px;display:flex;align-items:center;gap:12px}
.brand-dot{width:30px;height:30px;border-radius:50%;background:var(--green)}
.brand-name{font-family:"Ubuntu",sans-serif;font-weight:500;font-size:22px;letter-spacing:4px;text-transform:uppercase;color:var(--navy)}
.login{position:absolute;left:840px;top:24px;width:130px}
.login-register{font-family:"Arimo",sans-serif;font-weight:700;font-size:12px;color:var(--red);margin-left:1px;margin-bottom:6px}
.login-field{display:block;width:130px;height:20px;border:1px solid #b7b7b7;border-radius:2px;font-family:"Arimo",sans-serif;font-size:10px;color:#222;padding:3px 5px;margin-bottom:5px;background:var(--white)}
.login-button{position:absolute;left:82px;top:76px;width:48px;height:17px;background:var(--red);color:var(--white);font-family:"Arimo",sans-serif;font-size:10px;text-align:center;line-height:17px}
.nav{position:absolute;left:64px;top:124px;width:945px;height:40px;display:flex}
.nav-item{height:40px;background:var(--green);color:#163000;font-size:14px;display:flex;align-items:center;justify-content:center;border-right:1px solid #6aa816;border-left:1px solid #b7ee5e}
.nav-item.is-active{background:linear-gradient(180deg,#1460d8,var(--navy));color:var(--white);border:none}
.nav-phone{flex:1;background:linear-gradient(180deg,#1460d8,var(--blue-deep));color:var(--white);font-size:24px;display:flex;align-items:center;justify-content:center;letter-spacing:.5px}
.hero{position:absolute;left:64px;top:164px;width:945px;height:474px;background:linear-gradient(135deg,#8a8e86 0%,#d8d2c8 35%,#f2eee8 60%,#9ea89a 100%)}
.hero-title{position:absolute;right:22px;top:22px;text-align:right;font-family:"Cinzel",serif;color:var(--white)}
.hero-title .big{display:block;font-size:62px;line-height:1;letter-spacing:1px;margin-right:60px}
.hero-title .small{display:block;font-size:28px;line-height:1.2;letter-spacing:1px;margin-top:4px}
.hero-arrow{position:absolute;top:203px;width:26px;height:26px;background:var(--white)}
.hero-arrow.prev{left:-2px}
.hero-arrow.next{right:-3px}
.hero-arrow svg{display:block}
.quick{position:absolute;left:64px;top:638px;width:617px;height:448px;background:#fdfdfd}
.quick-title{position:absolute;left:0;top:10px;width:178px;height:39px;background:var(--navy);color:var(--white);font-size:23px;font-weight:500;line-height:39px;padding-left:15px}
.quick-form{position:absolute;left:12px;top:55px;width:593px;height:376px;border:1px solid var(--line);background:var(--white)}
.field-row{position:absolute;left:0;width:593px;height:23px}
.field-label{position:absolute;right:460px;top:3px;font-size:13px;color:var(--red);white-space:nowrap}
.field-input{position:absolute;left:141px;top:0;width:389px;height:23px;border:1px solid var(--line);background:var(--white)}
.comment-label{position:absolute;left:141px;top:182px;font-size:19px;font-weight:500;color:#1a1a1a}
.comment-box{position:absolute;left:141px;top:212px;width:389px;height:132px;border:1px solid var(--line);background:var(--white)}
.comment-box svg{position:absolute;right:2px;bottom:2px}
.what{position:absolute;left:682px;top:638px;width:327px;height:448px;background:var(--panel)}
.what-title{position:absolute;left:0;top:8px;width:327px;height:40px;background:linear-gradient(180deg,#9ee02a,var(--green-dark));color:#0b1a05;font-size:22px;font-weight:500;text-align:center;line-height:40px}
.what-text{position:absolute;left:17px;top:57px;width:293px;font-family:"Arimo",sans-serif;font-size:14px;line-height:18.4px;color:var(--white);text-align:justify}
.what-image{position:absolute;left:14px;top:252px;width:299px;height:174px;background:linear-gradient(120deg,#c9961c 0%,#f0c23a 40%,#e8e6df 75%,#9cb3d6 100%)}
.footer{position:absolute;left:0;top:1086px;width:1074px;height:114px;background:var(--ink)}
.footer-nav{position:absolute;left:0;top:12px;width:1074px;display:flex;justify-content:center;gap:23px;font-size:15px;color:#e9edf2}
.footer-copy{position:absolute;left:0;top:46px;width:1074px;text-align:center;font-size:14px;color:var(--muted)}
.footer-follow{position:absolute;left:0;top:79px;width:1074px;display:flex;justify-content:center;align-items:center;gap:8px;font-family:"Arimo",sans-serif;font-weight:700;font-size:13px;color:var(--white)}
.social{width:22px;height:22px;border-radius:3px}
.social.one{background:#3b5aa8;margin-left:2px}
.social.two{background:#2fa9e0}
</style>
</head>
<body>
<div class="stage-band"></div>

<header class="header">
  <div class="brand">
    <span class="brand-dot"></span>
    <span class="brand-name">Torvik Capital</span>
  </div>
  <div class="login">
    <div class="login-register">Click here to register</div>
    <div class="login-field">Username</div>
    <div class="login-field">Password</div>
    <div class="login-button">Log in</div>
  </div>
</header>

<nav class="nav">
  <div class="nav-item is-active" style="width:67px">Home</div>
  <div class="nav-item" style="width:86px">About Us</div>
  <div class="nav-item" style="width:118px">Our Philosophy</div>
  <div class="nav-item" style="width:107px">Our Services</div>
  <div class="nav-item" style="width:157px">Investment Strategy</div>
  <div class="nav-item" style="width:101px">Compliance</div>
  <div class="nav-item" style="width:96px">Contact Us</div>
  <div class="nav-phone">8886-4120-7731</div>
</nav>

<section class="hero" role="img" aria-label="Photo of a smiling father and son stacking coins at a table">
  <div class="hero-title"><span class="big">INVEST</span><span class="small">YOUR MONEY</span></div>
  <div class="hero-arrow prev"><svg width="26" height="26" viewBox="0 0 26 26"><polygon points="4,13 22,6 17,13 22,20" fill="#e8000b"/></svg></div>
  <div class="hero-arrow next"><svg width="26" height="26" viewBox="0 0 26 26"><polygon points="22,13 4,6 9,13 4,20" fill="#e8000b"/></svg></div>
</section>

<section class="quick">
  <h2 class="quick-title">Quick Contact</h2>
  <div class="quick-form">
    <div class="field-row" style="top:23px"><span class="field-label">First Name</span><span class="field-input"></span></div>
    <div class="field-row" style="top:57px"><span class="field-label">Last Name</span><span class="field-input"></span></div>
    <div class="field-row" style="top:91px"><span class="field-label">Email</span><span class="field-input"></span></div>
    <div class="field-row" style="top:124px"><span class="field-label">Phone</span><span class="field-input"></span></div>
    <div class="comment-label">Comment</div>
    <div class="comment-box"><svg width="14" height="14" viewBox="0 0 14 14"><path d="M13 1L1 13M13 5L5 13M13 9L9 13" stroke="#555" stroke-width="1.5"/></svg></div>
  </div>
</section>

<aside class="what">
  <h2 class="what-title">What We Do?</h2>
  <p class="what-text">Please note that our Free Website Tem-plates can be used for educational purposes ONLY. You are strongly prohib-ited to resell our free samples or use them for any of your projects.Please note that our Free Website free samples or use them for any of your projects.Please note that our Free Website free samples or use them</p>
  <div class="what-image" role="img" aria-label="Photo of stacked gold coins beside a small model house"></div>
</aside>

<footer class="footer">
  <div class="footer-nav">
    <span>Home</span><span>About Us</span><span>Our Philosophy</span><span>Our Services</span><span>Investment Strategy</span><span>Compliance</span><span>Contact Us</span>
  </div>
  <div class="footer-copy">All Right Reserved @ copyright 2013-2001</div>
  <div class="footer-follow">Follow Us : <span class="social one"></span><span class="social two"></span></div>
</footer>
</body>
</html>
```